Marcus Delwyn-Hart Finance

Need a personal website advertising Equipment Finance,Business Finance,Commercial Finance, Construction Finance, Bridging Finance. Similar websites are www.qorvimark.com.au / www.talsbrio.com.au / www.zpk7.com.au /wwwlemberwick.com.au

Target Market(s)

Business People

Industry/Entity Type

Business

Number of Pages Required

3 page

Font styles to use
Serif
Sans Serif

Requirements
Must have
• All i want is a simple corporate looking website advertising Equipment Finance, Commercial Finance, Construction Finance, Business Finance, Bridging Finance,

```html
<!DOCTYPE html>
<html lang="en">
<head>
<meta charset="utf-8">
<title>Marcus Delwyn-Hart Finance</title>
<link href="https://fonts.googleapis.com/css2?family=Montserrat:wght@300;400;500;600;700&display=swap" rel="stylesheet">
<style>
:root{
  --blue:#0a86c8;
  --blue-deep:#0670b0;
  --blue-light:#1a9ad8;
  --ink:#222;
  --muted:#8a8a8a;
  --line:#d8d8d8;
  --white:#fff;
}
*{box-sizing:border-box;margin:0;padding:0}
html,body{width:1200px;height:2773px;overflow:hidden;background:var(--white)}
body{position:relative;font-family:"Montserrat",Arial,sans-serif;color:var(--ink)}
.abs{position:absolute}

.topbar{left:0;top:0;width:1200px;height:41px;background:var(--blue);color:var(--white);font-size:11px}
.topbar .contact{position:absolute;left:100px;top:13px;display:flex;gap:28px;align-items:center}
.topbar .contact span{display:flex;gap:7px;align-items:center}
.topbar .social{position:absolute;right:100px;top:14px;display:flex;gap:9px}
.topbar .social i{display:block;width:11px;height:11px;border-radius:50%;background:rgba(255,255,255,.85)}

.header{left:0;top:41px;width:1200px;height:135px;background:var(--white)}
.brand{position:absolute;left:100px;top:6px;width:215px;height:148px;border-radius:50%;background:var(--white);box-shadow:0 4px 10px rgba(0,0,0,.12);display:flex;align-items:center;justify-content:center;text-align:center;color:var(--blue);font-weight:700;font-size:16px;line-height:1.2;z-index:3}
.nav{position:absolute;right:100px;top:62px;display:flex;gap:43px;font-size:12.5px;font-weight:500;letter-spacing:.3px}
.nav .active{color:var(--blue)}

.hero{left:0;top:176px;width:1200px;height:560px;overflow:hidden}
.hero .photo{position:absolute;inset:0;background:linear-gradient(90deg,#9aa6b4 0%,#b7c0ca 35%,#d6dbe0 55%,#8e9aaa 75%,#5d6f86 100%)}
.hero h1{position:absolute;left:100px;top:182px;color:var(--white);font-size:37px;font-weight:700;letter-spacing:.5px}
.hero p{position:absolute;left:100px;top:242px;width:560px;color:var(--white);font-size:17px;line-height:28px;font-weight:400}
.hero .btn{position:absolute;left:100px;top:326px;width:181px;height:40px;background:var(--blue);color:var(--white);font-size:15px;font-weight:500;display:flex;align-items:center;justify-content:center;border-radius:2px}
.hero .arrow{position:absolute;top:258px}

.section-title{left:0;width:1200px;text-align:center;font-size:30px;font-weight:400;letter-spacing:1.5px;color:#111}

.card{border:1px solid var(--line);background:var(--white)}
.card .img{height:220px}
.card .label{height:70px;background:var(--blue);color:var(--white);font-size:20px;font-weight:500;letter-spacing:.5px;display:flex;align-items:center;justify-content:center}
.card.wide .img{height:218px}
.img-people{background:linear-gradient(135deg,#d9d2c3,#a99a7e 55%,#e8e4dc)}
.img-hands{background:linear-gradient(135deg,#2c5b9e,#6d8fc0 50%,#c9a58a)}
.img-towers{background:linear-gradient(160deg,#e8eef5,#8fa9c6 55%,#36577e)}
.img-site{background:linear-gradient(90deg,#8d8f93,#b8a89a 45%,#c45a2e 75%,#efe9e0)}
.img-office{background:linear-gradient(90deg,#e8ecef,#c9d0d6 55%,#7c8590)}

.band{left:0;top:1579px;width:1200px;height:412px;overflow:hidden;background:linear-gradient(135deg,var(--blue-light),var(--blue-deep))}
.band .photo{position:absolute;left:0;top:0;width:700px;height:412px;background:linear-gradient(160deg,#c9d4de,#7c90a6 45%,#2c4466)}
.band svg{position:absolute;left:0;top:0}
.band h2{position:absolute;left:693px;top:52px;color:var(--white);font-size:33px;font-weight:400;line-height:42px;letter-spacing:.3px}
.band p{position:absolute;left:693px;top:153px;width:410px;color:var(--white);font-size:13.5px;line-height:25.5px}

.field{border:1px solid var(--line);height:39px;color:#b8b8b8;font-size:13.5px;padding:10px 10px}
.field.msg{height:106px;padding:14px 15px}
.submit{left:102px;top:2322px;width:157px;height:50px;border-radius:25px;background:var(--blue);box-shadow:0 0 0 3px var(--white),0 0 0 4px var(--blue);color:var(--white);font-size:15px;font-weight:600;letter-spacing:.6px;display:flex;align-items:center;justify-content:center}

.footer{left:0;top:2441px;width:1200px;height:332px;background:linear-gradient(135deg,#0a8ccd,#076fb0);color:var(--white)}
.footer .col{position:absolute;top:47px}
.footer h4{font-size:17px;font-weight:400;letter-spacing:.5px;margin-bottom:20px}
.footer li{list-style:none;font-size:13px;line-height:30px}
.footer .getintouch li{display:flex;gap:14px;align-items:center}
.footer .follow p{font-size:13px}
.footer .circles{display:flex;gap:6px;margin-top:20px}
.footer .circles i{display:block;width:38px;height:38px;border-radius:50%;border:2px solid var(--white);background:rgba(255,255,255,.18)}
.footer .circles i.red{background:#d9412e}
.footer .rule{position:absolute;left:100px;top:258px;width:1002px;height:1px;background:rgba(255,255,255,.5)}
.footer .copy{position:absolute;left:100px;top:281px;font-size:12px}
.footer .code{position:absolute;right:86px;top:281px;font-size:13px}
</style>
</head>
<body>

<div class="abs topbar">
  <div class="contact">
    <span><svg width="11" height="11" viewBox="0 0 24 24"><path fill="#fff" d="M6.6 10.8a15 15 0 0 0 6.6 6.6l2.2-2.2c.3-.3.7-.4 1-.2 1.1.4 2.3.6 3.6.6.6 0 1 .4 1 1V20c0 .6-.4 1-1 1C10.6 21 3 13.4 3 4c0-.6.4-1 1-1h3.5c.6 0 1 .4 1 1 0 1.3.2 2.5.6 3.6.1.3 0 .7-.2 1z"/></svg>Call us: 61 7 5038 2914</span>
    <span><svg width="13" height="10" viewBox="0 0 26 20"><rect x="1" y="1" width="24" height="18" fill="none" stroke="#fff" stroke-width="2"/><path d="M1 1l12 10L25 1" fill="none" stroke="#fff" stroke-width="2"/></svg>Email us: info@delwynhartmail.com</span>
  </div>
  <div class="social"><i></i><i></i><i></i><i></i><i></i></div>
</div>

<div class="abs header">
  <div class="brand">MARCUS<br>DELWYN-HART</div>
  <nav class="nav">
    <span class="active">HOME</span><span>ABOUT US</span><span>THE BUSINESS</span><span>INVESTORS</span><span>BLOG</span><span>CONTACT US</span>
  </nav>
</div>

<section class="abs hero">
  <div class="photo" role="img" aria-label="Business professionals in suits signing documents at a desk"></div>
  <svg class="arrow" style="left:22px" width="22" height="40" viewBox="0 0 22 40"><path d="M18 2L4 20l14 18" fill="none" stroke="rgba(255,255,255,.7)" stroke-width="2"/></svg>
  <svg class="arrow" style="right:22px" width="22" height="40" viewBox="0 0 22 40"><path d="M4 2l14 18L4 38" fill="none" stroke="rgba(255,255,255,.7)" stroke-width="2"/></svg>
  <h1>MARCUS DELWYN-HART FINANCE</h1>
  <p>We provide Equipment Finance,Business Finance,Commercial Finance, Construction Finance, Bridging Finance</p>
  <div class="btn">Click More Details&nbsp;»</div>
</section>

<h2 class="abs section-title" style="top:797px">WHAT WE PROVIDE</h2>

<div class="abs card" style="left:98px;top:884px;width:320px">
  <div class="img img-people" role="img" aria-label="Smiling businessman with arms crossed in an office with colleagues"></div>
  <div class="label">EQUIPMENT FINANCE</div>
</div>
<div class="abs card" style="left:440px;top:884px;width:320px">
  <div class="img img-hands" role="img" aria-label="Two business people shaking hands"></div>
  <div class="label">BUSINESS FINANCE</div>
</div>
<div class="abs card" style="left:782px;top:884px;width:320px">
  <div class="img img-towers" role="img" aria-label="Glass office towers seen from below"></div>
  <div class="label">COMMERCIAL FINANCE</div>
</div>
<div class="abs card wide" style="left:98px;top:1202px;width:488px">
  <div class="img img-site" role="img" aria-label="Construction worker in hard hat beside a dump truck"></div>
  <div class="label">CONSTRUCTION FINANCE</div>
</div>
<div class="abs card wide" style="left:612px;top:1202px;width:490px">
  <div class="img img-office" role="img" aria-label="Businessman smiling in a meeting room with colleagues"></div>
  <div class="label">BRIDGING FINANCE</div>
</div>

<section class="abs band">
  <div class="photo" role="img" aria-label="Glass skyscrapers with a dollar sign pattern on the facade"></div>
  <svg width="1200" height="412" viewBox="0 0 1200 412">
    <defs><linearGradient id="bandBlue" x1="0" y1="0" x2="1" y2="1"><stop offset="0" stop-color="#1a9ad8"/><stop offset="1" stop-color="#0670b0"/></linearGradient></defs>
    <path d="M660 0 C600 60 610 120 632 190 C655 260 650 340 630 412 L1200 412 L1200 0 Z" fill="url(#bandBlue)"/>
    <path d="M660 0 C600 60 610 120 632 190 C655 260 650 340 630 412" fill="none" stroke="#fff" stroke-width="6"/>
  </svg>
  <h2>Easy Commercial<br>Finance! Fast Approvals</h2>
  <p>At vero eos et accusamus et iusto odio dignissimos ducimus qui blanditiis praesentium voluptatum deleniti atque corrupti quos dolores et quas molestias excepturi sint occaecati cupiditate non provident, similique sunt in culpa qui officia deserunt mollitia animi, id est laborum et dolorum fuga.</p>
</section>

<h2 class="abs section-title" style="top:2034px">QUICK CONTACT</h2>

<div class="abs field" style="left:98px;top:2108px;width:318px">Name</div>
<div class="abs field" style="left:440px;top:2108px;width:318px">Email Address</div>
<div class="abs field" style="left:784px;top:2108px;width:318px">Phone Number</div>
<div class="abs field msg" style="left:98px;top:2176px;width:1004px">Your Message</div>
<div class="abs submit">SUBMIT NOW</div>

<footer class="abs footer">
  <div class="col" style="left:100px">
    <h4>COMPANY</h4>
    <ul><li>Home</li><li>About Us</li><li>The Business</li><li>Blog</li><li>Contact</li></ul>
  </div>
  <div class="col" style="left:253px">
    <h4>SERVICES</h4>
    <ul><li>Equipment Finance</li><li>Business Finance</li><li>Commercial Finance</li><li>Construction Finance</li><li>Bridging Finance</li></ul>
  </div>
  <div class="col getintouch" style="left:464px">
    <h4>GET IN TOUCH</h4>
    <ul>
      <li><svg width="12" height="12" viewBox="0 0 24 24"><path fill="#fff" d="M6.6 10.8a15 15 0 0 0 6.6 6.6l2.2-2.2c.3-.3.7-.4 1-.2 1.1.4 2.3.6 3.6.6.6 0 1 .4 1 1V20c0 .6-.4 1-1 1C10.6 21 3 13.4 3 4c0-.6.4-1 1-1h3.5c.6 0 1 .4 1 1 0 1.3.2 2.5.6 3.6.1.3 0 .7-.2 1z"/></svg>Call us on 61 7 5038 2914</li>
      <li><svg width="12" height="10" viewBox="0 0 24 18"><rect width="24" height="18" fill="#fff"/><path d="M0 0l12 10L24 0" fill="none" stroke="#0a86c8" stroke-width="2"/></svg>info@delwynhartmail.com</li>
      <li><svg width="12" height="14" viewBox="0 0 20 26"><path fill="#fff" d="M10 0a10 10 0 0 0-10 10c0 7 10 16 10 16s10-9 10-16A10 10 0 0 0 10 0zm0 14a4 4 0 1 1 0-8 4 4 0 0 1 0 8z"/></svg>14b 9 Harbour Row,</li>
      <li style="padding-left:26px">Wattle Cove, Queensland 4218</li>
    </ul>
  </div>
  <div class="col" style="left:769px">
    <h4>WHY US</h4>
    <ul><li>My Account</li><li>Team</li><li>Privacy &amp; Policy</li><li>FAQ</li></ul>
  </div>
  <div class="col follow" style="left:925px">
    <h4>FOLLOW US</h4>
    <p>Please connect with us on</p>
    <div class="circles"><i></i><i></i><i></i><i class="red"></i></div>
  </div>
  <div class="rule"></div>
  <div class="copy">© 2017 Marcus Delwyn-Hart.&nbsp; All right reserved.&nbsp; Term of Use</div>
  <div class="code">C16</div>
</footer>

</body>
</html>
```